Android application design for shared calendar app

I need an Android app design for shared calendar, It should have a business look&feel,flat material design. Main part of UI are big clock-like wheels which represent free time and busy time. Busy is red ,free is green. App should have business look & feel but it should be still usable for non business users.

app can be seen here,please try it before starting design
https://apps.quellmarket.net/details?id=com.tidlomo&hl=en

here is a video: https://clipvane.example/v/Rk8pZq2LmTx

Target Market(s)

busy business professionals

Industry/Entity Type

Business

Font styles to use
Sans Serif

Requirements
Must have
• 1) project must have big clock-like circles in which free time is marked in green, busy time in red. so those colors must be green and red but you can use which shades.
• 2) project must have one 16:9 ratio image which has text : click here to load picture which describes your event. and under that text several pictures - business meeting, phone call,some people playing sports,some people in pub. I have attached how it currently look - don't use it, thats just a example :)
• 3) must have default placeholder for user image. I also attached how it currently looks
• 4) buttons and dialogs must be rounded - see how it looks in the app
• 5) events must have semi transparent overlay - see how it looks in the app. font for location and event name can be changed
• 6) App must use eurofurencebold regular for title in action bar., that can't be changed. App must use existing logo (green overlapping clocks)
Nice to have
• a loading page with progress bar should have some interesting picture (city for example)

```html
<!DOCTYPE html>
<html lang="en">
<head>
<meta charset="utf-8">
<title>Tidlomo – Today</title>
<link href="https://fonts.googleapis.com/css2?family=Roboto+Condensed:wght@400;700&display=swap" rel="stylesheet">
<style>
  :root {
    --page-bg: #16324f;
    --screen-top: #1d4a78;
    --screen-mid: #2b5e8f;
    --screen-bottom: #1a3d63;
    --bar-bg: #1b426b;
    --tab-line: #4a74a0;
    --text-light: #e6eef8;
    --text-soft: #b7cce3;
    --pill-bg: #8cc8f5;
    --pill-text: #153a5e;
    --free: #22e04a;
    --busy: #ef1b1b;
    --unset: #a9b3c4;
    --number-dark: #123016;
    --greeting: #bfe0ff;
    --avatar-fill: #6a4a33;
  }
  * { box-sizing: border-box; margin: 0; padding: 0; }
  html, body {
    width: 1108px; height: 1200px; overflow: hidden;
    background: var(--page-bg);
    font-family: "Roboto Condensed", "Arial Narrow", sans-serif;
  }
  .screen {
    position: absolute; left: 274px; top: 102px;
    width: 560px; height: 996px; overflow: hidden;
    background: radial-gradient(ellipse at 50% 40%, var(--screen-mid), var(--screen-top) 55%, var(--screen-bottom));
    color: var(--text-light);
  }
  .status-bar {
    height: 40px; display: flex; align-items: center; justify-content: space-between;
    padding: 0 16px; font-size: 17px; color: var(--text-light);
    background: var(--bar-bg);
  }
  .app-bar {
    height: 74px; display: flex; align-items: center; justify-content: center; gap: 12px;
    background: var(--bar-bg); border-bottom: 1px solid var(--tab-line);
  }
  .app-mark { width: 38px; height: 38px; border-radius: 50%; background: var(--free); border: 3px solid #fff; }
  .app-title { font-size: 36px; font-weight: 700; letter-spacing: 1px; color: var(--text-light); }
  .day-tabs { display: flex; height: 76px; border-bottom: 1px solid var(--tab-line); }
  .day-tab {
    flex: 1; display: flex; align-items: center; justify-content: center;
    font-size: 27px; color: var(--text-soft); border-right: 1px solid var(--tab-line);
  }
  .day-tab:last-child { border-right: none; }
  .day-tab.is-active { color: #fff; font-weight: 700; }
  .period-switch { display: flex; justify-content: center; gap: 90px; margin-top: 34px; }
  .period-button {
    width: 150px; height: 76px; border-radius: 10px;
    display: flex; align-items: center; justify-content: center;
    font-size: 44px; font-weight: 700;
  }
  .period-button.is-active { background: var(--pill-bg); color: var(--pill-text); box-shadow: 0 0 0 3px #cfe9ff inset; }
  .period-button.is-idle { background: rgba(255,255,255,0.06); color: rgba(20,50,85,0.7); border: 1px solid rgba(255,255,255,0.15); }
  .day-wheel { display: block; margin: 26px auto 0; }
  .wheel-number { font-size: 30px; font-weight: 700; fill: var(--number-dark); text-anchor: middle; dominant-baseline: central; }
  .wheel-number.is-light { fill: #fff; }
  .greeting-small { font-size: 20px; fill: var(--greeting); }
  .greeting-name, .greeting-line { font-size: 34px; font-weight: 700; fill: var(--greeting); text-anchor: middle; }
  .section-divider { margin: 22px 30px 0; border-top: 1px solid rgba(255,255,255,0.18); position: relative; }
  .label-pill {
    display: inline-block; background: var(--pill-bg); color: var(--pill-text);
    font-size: 17px; font-weight: 700; padding: 3px 16px; border-radius: 5px;
    border: 2px solid #d7eeff;
  }
  .stats-label { text-align: center; margin-top: -14px; }
  .stats-row { display: flex; justify-content: space-between; align-items: center; padding: 26px 36px 0 36px; }
  .user-avatar {
    width: 118px; height: 118px; border-radius: 50%;
    background: radial-gradient(circle at 50% 40%, var(--avatar-fill), #2e6b3a);
    border: 5px solid #fff;
  }
  .stat-item { display: flex; flex-direction: column; align-items: center; gap: 10px; }
</style>
</head>
<body>
<main class="screen">
  <div class="status-bar">
    <span>●●●●○ NORDA</span>
    <span>4:21 PM</span>
    <span>100% ▮</span>
  </div>

  <header class="app-bar">
    <span class="app-mark"></span>
    <span class="app-title">TIDLOMO</span>
  </header>

  <nav class="day-tabs">
    <div class="day-tab is-active">TODAY</div>
    <div class="day-tab">TOMORROW</div>
    <div class="day-tab">MONDAY</div>
  </nav>

  <div class="period-switch">
    <div class="period-button is-active">am</div>
    <div class="period-button is-idle">pm</div>
  </div>

  <svg class="day-wheel" width="360" height="360" viewBox="-180 -180 360 360" aria-label="Hour wheel">
    <defs>
      <path id="hour-segment" d="M -39.68 -165.3 A 170 170 0 0 1 39.68 -165.3 L 26.14 -108.9 A 112 112 0 0 0 -26.14 -108.9 Z" stroke="rgba(255,255,255,0.55)" stroke-width="1.5"/>
    </defs>
    <use href="#hour-segment" fill="var(--free)" transform="rotate(0)"/>
    <use href="#hour-segment" fill="var(--free)" transform="rotate(30)"/>
    <use href="#hour-segment" fill="var(--free)" transform="rotate(60)"/>
    <use href="#hour-segment" fill="var(--busy)" transform="rotate(90)"/>
    <use href="#hour-segment" fill="var(--busy)" transform="rotate(120)"/>
    <use href="#hour-segment" fill="var(--free)" transform="rotate(150)"/>
    <use href="#hour-segment" fill="var(--free)" transform="rotate(180)"/>
    <use href="#hour-segment" fill="var(--free)" transform="rotate(210)"/>
    <use href="#hour-segment" fill="var(--free)" transform="rotate(240)"/>
    <use href="#hour-segment" fill="var(--busy)" transform="rotate(270)"/>
    <use href="#hour-segment" fill="var(--busy)" transform="rotate(300)"/>
    <use href="#hour-segment" fill="var(--unset)" transform="rotate(330)"/>

    <text class="wheel-number" x="0" y="-141">13</text>
    <text class="wheel-number" x="70.5" y="-122.1">14</text>
    <text class="wheel-number is-light" x="122.1" y="-70.5">15</text>
    <text class="wheel-number is-light" x="141" y="0">16</text>
    <text class="wheel-number" x="122.1" y="70.5">17</text>
    <text class="wheel-number" x="70.5" y="122.1">18</text>
    <text class="wheel-number" x="0" y="141">19</text>
    <text class="wheel-number" x="-70.5" y="122.1">20</text>
    <text class="wheel-number is-light" x="-122.1" y="70.5">21</text>
    <text class="wheel-number is-light" x="-141" y="0">22</text>
    <text class="wheel-number is-light" x="-122.1" y="-70.5">23</text>
    <text class="wheel-number" x="-70.5" y="-122.1">24</text>

    <text class="greeting-name" x="0" y="-4"><tspan class="greeting-small">Hi </tspan>STELLAN</text>
    <text class="greeting-line" x="0" y="38">God kväll</text>
  </svg>

  <div class="section-divider"></div>
  <div class="stats-label"><span class="label-pill">STATICS</span></div>

  <section class="stats-row">
    <div class="user-avatar" role="img" aria-label="User profile photo"></div>
    <div class="stat-item">
      <svg width="124" height="124" viewBox="0 0 124 124" aria-label="Busy time today">
        <circle cx="62" cy="62" r="52" fill="none" stroke="var(--busy)" stroke-width="12" stroke-dasharray="25.2 2"/>
      </svg>
      <span class="label-pill">TODAY</span>
    </div>
    <div class="stat-item">
      <svg width="124" height="124" viewBox="0 0 124 124" aria-label="Free time yesterday">
        <circle cx="62" cy="62" r="52" fill="none" stroke="var(--free)" stroke-width="12" stroke-dasharray="25.2 2"/>
      </svg>
      <span class="label-pill">YESTERDAY</span>
    </div>
  </section>
</main>
</body>
</html>
```